Business Card Design

Please see my website www.qvloreming.com.au to for further information on my services and styling of my site

Reason: Deadline is extended to permit alterations to current designs or for any new submissions. Cheers

Industry/Entity Type

Business

Contact Information for Business Card

Marcus Thorne
Empowerment Coach

'Live your passion'

marcus@qvtraining.com.au
0437158204
qvtraining.com.au

```html
<!DOCTYPE html>
<html lang="en">
<head>
<meta charset="UTF-8">
<title>QVT Business Card</title>
<link href="https://fonts.googleapis.com/css2?family=Open+Sans:wght@300;400;600&display=swap" rel="stylesheet">
<style>
  :root {
    --backdrop: #6e6e6e;
    --card-white: #ffffff;
    --charcoal: #5c5c5c;
    --charcoal-deep: #4f4f4f;
    --lime: #9acd32;
    --silver: #d2d2d2;
    --ink-soft: #6a6a6a;
    --rule: #bdbdbd;
    --placeholder-top: #666666;
    --placeholder-bottom: #5a5a5a;
  }
  * { margin: 0; padding: 0; box-sizing: border-box; }
  html, body {
    width: 1200px; height: 750px; overflow: hidden;
    background: var(--backdrop);
    font-family: "Open Sans", Arial, sans-serif;
  }
  .stage {
    width: 1200px; height: 750px;
    display: flex; align-items: center; justify-content: center; gap: 40px;
  }
  .card {
    position: relative;
    width: 540px; height: 309px;
    overflow: hidden;
    box-shadow: 0 10px 24px rgba(0,0,0,0.35);
  }

  /* ---------- Contact side ---------- */
  .card--contact { background: var(--card-white); }
  .card--contact .band-charcoal {
    position: absolute; left: 0; right: 0; top: 128px; height: 116px;
    background: var(--charcoal);
  }
  .card--contact .band-lime {
    position: absolute; left: 0; right: 0; top: 250px; height: 34px;
    background: var(--lime);
  }
  .brand {
    position: absolute; left: 150px; top: 34px;
    display: flex; align-items: center; gap: 10px;
  }
  .brand__mark {
    width: 14px; height: 14px; border-radius: 50%;
    background: var(--lime);
  }
  .brand__text { display: flex; flex-direction: column; }
  .brand__initials {
    font-size: 40px; line-height: 1; font-weight: 400;
    color: var(--lime); letter-spacing: 2px;
  }
  .brand__name {
    margin-top: 4px; padding-top: 3px;
    border-top: 1px solid var(--rule);
    font-size: 13px; font-weight: 400; color: var(--ink-soft);
  }
  .person {
    position: absolute; right: 28px; top: 140px; text-align: right;
    color: var(--card-white);
  }
  .person__name { font-size: 20px; font-weight: 300; letter-spacing: 1px; text-transform: uppercase; }
  .person__role { font-size: 10px; font-weight: 300; color: var(--silver); }
  .contact {
    position: absolute; left: 26px; top: 178px;
    color: var(--card-white); font-size: 11px; font-weight: 300;
  }
  .contact__row { display: flex; align-items: flex-start; gap: 10px; margin-bottom: 8px; }
  .contact__row svg { flex: none; }
  .contact__lines { line-height: 1.3; }

  /* ---------- Brand side ---------- */
  .card--brand { background: var(--charcoal); }
  .card--brand .band-white {
    position: absolute; left: 0; right: 0; top: 70px; height: 118px;
    background: var(--card-white);
  }
  .emblem {
    position: absolute; left: 40px; top: 62px; width: 170px; height: 138px;
    background: var(--charcoal-deep);
  }
  .emblem__initials {
    position: absolute; left: 14px; top: 12px;
    font-size: 30px; line-height: 1; font-weight: 400; color: var(--lime); letter-spacing: 2px;
  }
  .emblem__artwork {
    position: absolute; left: 14px; right: 14px; top: 52px; bottom: 12px;
    background: linear-gradient(180deg, var(--placeholder-top), var(--placeholder-bottom));
  }
  .card--brand .brand { left: 290px; top: 92px; }
  .card--brand .brand__initials { font-size: 34px; }
  .card--brand .brand__name { font-size: 11px; }
</style>
</head>
<body>
<main class="stage">

  <section class="card card--contact">
    <div class="band-charcoal"></div>
    <div class="band-lime"></div>

    <div class="brand">
      <span class="brand__mark"></span>
      <div class="brand__text">
        <span class="brand__initials">QVT</span>
        <span class="brand__name">Quest &amp; Vitality Training</span>
      </div>
    </div>

    <div class="person">
      <p class="person__name">Marcus Thorne</p>
      <p class="person__role">Empowerment Coach</p>
    </div>

    <div class="contact">
      <div class="contact__row">
        <svg width="18" height="14" viewBox="0 0 18 14" aria-hidden="true">
          <path d="M1 5 Q9 -1 17 5 L15 7 L12 5 L6 5 L3 7 Z" fill="#fff"/>
          <rect x="4" y="7" width="10" height="6" rx="1" fill="#fff"/>
        </svg>
        <div class="contact__lines">0437158204</div>
      </div>
      <div class="contact__row">
        <svg width="18" height="18" viewBox="0 0 18 18" aria-hidden="true" fill="none" stroke="#fff" stroke-width="1.2">
          <circle cx="9" cy="9" r="8"/>
          <ellipse cx="9" cy="9" rx="3.5" ry="8"/>
          <line x1="1" y1="9" x2="17" y2="9"/>
          <line x1="2.5" y1="5" x2="15.5" y2="5"/>
          <line x1="2.5" y1="13" x2="15.5" y2="13"/>
        </svg>
        <div class="contact__lines">
          <p>marcus@qvtraining.com.au</p>
          <p>www.qvtraining.com.au</p>
        </div>
      </div>
    </div>
  </section>

  <section class="card card--brand">
    <div class="band-white"></div>

    <div class="emblem">
      <span class="emblem__initials">QVT</span>
      <div class="emblem__artwork" role="img" aria-label="Brand artwork area"></div>
    </div>

    <div class="brand">
      <span class="brand__mark"></span>
      <div class="brand__text">
        <span class="brand__initials">QVT</span>
        <span class="brand__name">Quest &amp; Vitality Training</span>
      </div>
    </div>
  </section>

</main>
</body>
</html>
```